Online video and marketing company business cards

Need to get some new business cards designed to fit with our new logo. The cards should be professional, clean and simple.

Cards should have:

Name
Position
2 line address
telephone
mobile
email address
web address

We need to have our logo and if possible say what we do...
ONLINE FILM PRODUCTION & STRATEGY

Industry/Entity Type

Marketing

```html
<!DOCTYPE html>
<html lang="en">
<head>
<meta charset="utf-8">
<title>lumenreel business cards</title>
<link rel="stylesheet" href="https://fonts.googleapis.com/css2?family=Open+Sans:wght@400;600;700&display=swap">
<style>
  :root {
    --backdrop: #2a2a2a;
    --navy: #003f66;
    --teal: #3f95a8;
    --teal-light: #5fb2c2;
    --tagline: #4f8fae;
    --ink: #1f3550;
    --address-ink: #3a4a5c;
    --paper: #ffffff;
    --paper-shade: #e9ecee;
  }
  * { margin: 0; padding: 0; box-sizing: border-box; }
  html, body {
    width: 1200px; height: 900px; overflow: hidden;
    background: var(--backdrop);
    font-family: "Open Sans", Arial, sans-serif;
  }
  .stage {
    width: 1200px; height: 900px;
    display: flex; flex-direction: column;
    align-items: center; justify-content: center; gap: 48px;
  }
  .card {
    position: relative;
    width: 660px; height: 377px;
    overflow: hidden;
    box-shadow: 0 10px 24px rgba(0,0,0,.45);
  }

  /* Front */
  .card-front { background: var(--navy); }
  .card-front .tagline {
    position: absolute; top: 38px; right: 46px;
    text-align: right;
    color: var(--tagline);
    font-size: 14px; letter-spacing: .06em; line-height: 1.4;
    text-transform: uppercase;
  }
  .card-front .brand {
    position: absolute; right: 46px; top: 160px;
    display: flex; align-items: center; gap: 18px;
  }
  .card-front .brand-dot {
    width: 54px; height: 54px; border-radius: 50%;
    background: var(--paper);
  }
  .card-front .brand-name {
    color: var(--teal-light);
    font-size: 58px; font-weight: 700; letter-spacing: -.02em;
    line-height: 1;
  }

  /* Back */
  .card-back {
    background: linear-gradient(120deg, var(--paper) 40%, var(--paper-shade) 100%);
    color: var(--ink);
  }
  .card-back .brand-name {
    position: absolute; left: 46px; top: 36px;
    color: var(--teal);
    font-size: 44px; font-weight: 700; letter-spacing: -.02em;
  }
  .card-back .person { position: absolute; left: 46px; top: 140px; }
  .card-back .person-name { color: var(--teal); font-size: 21px; font-weight: 600; }
  .card-back .person-role { font-size: 18px; margin-top: 2px; }
  .card-back .contact {
    position: absolute; left: 46px; top: 218px;
    font-size: 18px; line-height: 1.45;
    list-style: none;
  }
  .card-back .contact-label {
    display: inline-block; width: 24px; color: var(--teal);
  }
  .card-back .address {
    position: absolute; right: 46px; top: 140px;
    font-size: 17px; line-height: 1.45; font-style: normal;
    color: var(--address-ink);
  }
  .card-back .band {
    position: absolute; left: 0; right: 0; bottom: 0;
    height: 30px; background: var(--teal);
  }
</style>
</head>
<body>
<main class="stage">
  <section class="card card-front" aria-label="Card front">
    <p class="tagline">Online film<br>production &amp; strategy</p>
    <div class="brand">
      <span class="brand-dot"></span>
      <span class="brand-name">lumenreel</span>
    </div>
  </section>

  <section class="card card-back" aria-label="Card back">
    <div class="brand-name">lumenreel</div>
    <div class="person">
      <p class="person-name">Daniel Morrow</p>
      <p class="person-role">managing director</p>
    </div>
    <ul class="contact">
      <li><span class="contact-label">p</span>0207 946 0321</li>
      <li><span class="contact-label">m</span>0779 412 6083</li>
      <li><span class="contact-label">e</span>dmorrow@lumenreel.com</li>
    </ul>
    <address class="address">
      14, Harlow Row<br>
      London E2 7QL U.K.<br>
      www.lumenreel.com
    </address>
    <div class="band"></div>
  </section>
</main>
</body>
</html>
```